Pocket togo Menu Design Project. Must bring menu to look tasty with minimal pictures.

Kumo Garden to go menu pocket size. 10 inches x 4 inches folded in to 4 pages front and back @ 2.5 inches x 4 inches. full color

Target Market(s)

young professionals, modern taste, but not too radical for older people.

Font styles to use
Sans Serif

Colors

Designer to choose colors to be used in the design.

Requirements
Must have
• Simplicity but professional... I know that is the hardest thing to do. Pocket menu is going to be small... So big fonts or stand out color will be good. Restaurant is not big. Most of our customers are local regulars. I need to have a map (caroonish?) because we are located in small strip mall. So first timers have hard time finding us. Make sure to include lo-kart and the library next to us.
Nice to have
• Because out menu items are not much... Maybr one page could be a coupon?

```html
<!DOCTYPE html>
<html lang="en">
<head>
<meta charset="utf-8">
<title>Kumo Garden – To Go Menu</title>
<link href="https://fonts.googleapis.com/css2?family=Montserrat:ital,wght@0,300;0,400;0,600;0,800;1,800&display=swap" rel="stylesheet">
<style>
  :root {
    --page: #e6e6e6;
    --panel: #111111;
    --ink: #ffffff;
    --muted: #d8d8d8;
    --red: #e31e24;
    --blossom: #b5121b;
    --food-warm: #a8703a;
    --food-gold: #d9a441;
    --food-plate: #e9e1d2;
  }
  * { margin: 0; padding: 0; box-sizing: border-box; }
  html, body { width: 1200px; height: 900px; overflow: hidden; }
  body {
    background: var(--page);
    font-family: "Montserrat", sans-serif;
    color: var(--ink);
    position: relative;
  }
  .panel {
    position: absolute;
    top: 30px;
    width: 341px;
    height: 823px;
    background: var(--panel);
    overflow: hidden;
  }
  .panel--menu { left: 238px; }
  .panel--info { left: 637px; }

  .blossom {
    position: absolute;
    background: radial-gradient(ellipse at center, rgba(181,18,27,0.55), rgba(181,18,27,0) 70%);
  }

  .brand {
    position: absolute;
    display: flex;
    align-items: center;
    justify-content: center;
  }
  .brand__disc { position: absolute; border-radius: 50%; background: var(--red); }
  .brand__name {
    position: relative;
    font-weight: 800;
    color: var(--ink);
    text-transform: uppercase;
    white-space: nowrap;
  }

  .address {
    position: absolute; left: 0; width: 100%;
    text-align: center; font-size: 6.5px; line-height: 8px; font-weight: 400;
  }

  .section-title {
    position: absolute; left: 0; width: 100%;
    text-align: center;
    font-size: 16px; font-weight: 400; letter-spacing: 4px;
  }

  .menu-list { position: absolute; left: 37px; width: 281px; list-style: none; }
  .menu-item {
    display: grid;
    grid-template-columns: 1fr 40px 40px;
    height: 13.4px;
    font-size: 11px;
    font-weight: 400;
    line-height: 13.4px;
    white-space: nowrap;
  }
  .menu-item em { font-style: italic; font-weight: 800; font-size: 10px; text-transform: lowercase; }
  .menu-item small { font-size: 5px; letter-spacing: 0.2px; }
  .menu-list--two .menu-item { grid-template-columns: 1fr 40px; }

  .col-heads {
    position: absolute; left: 275px; width: 80px;
    display: grid; grid-template-columns: 40px 40px;
    font-size: 6px; color: var(--muted);
  }

  .notes {
    position: absolute; left: 37px;
    font-size: 7.5px; line-height: 9.5px; font-weight: 400;
  }
  .combo-desc {
    position: absolute; left: 55px;
    font-size: 7px; line-height: 8px; text-transform: uppercase;
  }

  .photo-strip {
    position: absolute; left: 0; width: 341px; height: 97px;
    display: grid; grid-template-columns: 77px 82px 88px 94px;
  }
  .photo { height: 100%; }
  .photo--chicken { background: linear-gradient(135deg, #6b4a2a, var(--food-warm) 60%, #efe9e0); }
  .photo--curry { background: radial-gradient(circle at 45% 45%, #f1e6c8 30%, var(--food-gold) 60%, #bf6b1e); }
  .photo--katsu { background: linear-gradient(160deg, #e5ead6 20%, #d98c2b 55%, #3a2a1c); }
  .photo--gyoza { background: linear-gradient(150deg, #b9a07a, var(--food-plate) 50%, #c9a87a); }

  .map {
    position: absolute; left: 39px; top: 480px; width: 134px; height: 112px;
    background: linear-gradient(135deg, #e8e6e1, #d9d6cf);
  }
  .location {
    position: absolute; left: 185px; top: 481px;
    font-size: 8.5px; line-height: 10.5px; font-weight: 400;
  }
  .location strong { font-weight: 800; display: block; }
  .location p + p { margin-top: 6px; }

  .cut-line {
    position: absolute; left: 6px; top: 607px; width: 329px; height: 10px;
  }

  .coupon__lead {
    position: absolute; left: 32px; top: 633px;
    font-size: 24px; font-weight: 800; letter-spacing: 0.3px;
  }
  .coupon__deal {
    position: absolute; left: 32px; top: 655px;
    font-weight: 800; color: var(--red); line-height: 1;
  }
  .coupon__deal .pct { font-size: 62px; letter-spacing: -1px; }
  .coupon__deal .off { font-size: 30px; position: relative; top: -28px; margin-left: 2px; }
  .coupon__terms {
    position: absolute; left: 32px; top: 720px;
    font-size: 9.5px; line-height: 12px; font-weight: 600;
  }
  .coupon__valid { color: var(--red); font-weight: 800; }
  .coupon__call { color: var(--red); font-weight: 800; font-size: 7px; display: block; margin-top: 1px; }
  .coupon__phone {
    position: absolute; left: 30px; top: 781px;
    font-size: 21px; font-weight: 800;
  }
</style>
</head>
<body>

<section class="panel panel--menu">
  <div class="blossom" role="img" aria-label="Cherry blossom branch" style="left:-10px;top:10px;width:120px;height:100px"></div>
  <div class="blossom" role="img" aria-label="Cherry blossom branch" style="left:245px;top:120px;width:110px;height:90px"></div>

  <div class="brand" style="left:106px;top:50px;width:120px;height:120px">
    <span class="brand__disc" style="width:120px;height:120px;left:0;top:0"></span>
    <span class="brand__name" style="font-size:24px">Kumo Garden</span>
  </div>

  <p class="address" style="top:186px">2140 NE Alder St, Fernwood, WA 98099<br>Phone: (425) 555-0142</p>

  <h2 class="section-title" style="top:216px">TERIYAKI</h2>
  <div class="col-heads" style="top:235px"><span>Regular</span><span>Large</span></div>
  <ul class="menu-list" style="top:244px">
    <li class="menu-item"><span>1. CHICKEN TERIYAKI</span><span>7.50</span><span>8.75</span></li>
    <li class="menu-item"><span>2. BEEF TERIYAKI</span><span>7.99</span><span>9.25</span></li>
    <li class="menu-item"><span>3. PORK TERIYAKI</span><span>7.75</span><span>9.25</span></li>
    <li class="menu-item"><span>4. SHRIMP TERIYAKI</span><span>7.99</span><span>9.25</span></li>
    <li class="menu-item"><span>5. CHICKEN BREAST</span><span>7.75</span><span>8.99</span></li>
    <li class="menu-item"><span>6. CHICKEN KATSU/TON KATSU</span><span></span><span>9.75</span></li>
    <li class="menu-item"><span>7. SHORT RIB TERIYAKI</span><span></span><span>12.50</span></li>
    <li class="menu-item"><span>8. CURRY CHICKEN</span><span>8.49</span><span></span></li>
    <li class="menu-item"><span>9. GYOZA PLATE</span><span>7.25</span><span>8.49</span></li>
    <li class="menu-item"><span>10. KATSU COMBO (W/#1,2,4,9)</span><span></span><span>10.25</span></li>
    <li class="menu-item"><span>11. BULGOGI</span><span></span><span>10.25</span></li>
  </ul>

  <div class="photo-strip" style="top:413px">
    <div class="photo photo--chicken" role="img" aria-label="Photo of chicken teriyaki with mushrooms"></div>
    <div class="photo photo--curry" role="img" aria-label="Photo of rice with curry chicken"></div>
    <div class="photo photo--katsu" role="img" aria-label="Photo of chicken katsu with cabbage"></div>
    <div class="photo photo--gyoza" role="img" aria-label="Photo of gyoza dumplings on a plate"></div>
  </div>

  <h2 class="section-title" style="top:515px">COMBINATION</h2>
  <ul class="menu-list" style="top:545px">
    <li class="menu-item"><span>12. COMBO</span><span></span><span>9.75</span></li>
  </ul>
  <p class="combo-desc" style="top:560px">Any combination of chicken, beef, pork<br>gyoza, shrimp your coice of 2 items</p>

  <div class="blossom" role="img" aria-label="Cherry blossom branch" style="left:250px;top:545px;width:100px;height:80px"></div>

  <h2 class="section-title" style="top:622px">STIR- FRY TERIYAKI</h2>
  <div class="col-heads" style="top:645px"><span>Regular</span><span>Large</span></div>
  <ul class="menu-list" style="top:650px">
    <li class="menu-item"><span>13. VEGETARIAN PATE <small>(ADD TOFU)</small></span><span>1.00</span><span>9.75</span></li>
    <li class="menu-item"><span>14. CHICKEN <em>with</em> VEGETABLES</span><span>8.99</span><span></span></li>
    <li class="menu-item"><span>15. BEEF <em>with</em> VEGETABLES</span><span></span><span>9.25</span></li>
    <li class="menu-item"><span>16. SHRIMP <em>with</em> VEGETABLES</span><span></span><span>9.25</span></li>
    <li class="menu-item"><span>17. YAKISOBA <small>(STIR FRIED NOODLES + VEG &amp; CHICKEN OR BEEF)</small></span><span></span><span>9.75</span></li>
    <li class="menu-item"><span>18. FRIED RICE <small>(WITH CHICKEN OR PORK)</small></span><span></span><span>9.25</span></li>
    <li class="menu-item"><span>19. CHICKEN BOWL</span><span></span><span>6.25</span></li>
    <li class="menu-item"><span>20.FRIED RICE</span><span></span><span>3.50</span></li>
    <li class="menu-item"><span>21. STIR FRIED VEGETABLE</span><span></span><span>4.99</span></li>
    <li class="menu-item"><span>* EXTRA CHICKEN</span><span></span><span>1.99</span></li>
  </ul>
  <p class="notes" style="top:784px">* HOT AND SPICY VAILABLE ON ALL ITEMS<br>* ALL MEALS ARE SERVED WITH RICE AND SALAD</p>
</section>

<section class="panel panel--info">
  <div class="blossom" role="img" aria-label="Cherry blossom branch" style="left:-10px;top:5px;width:120px;height:90px"></div>

  <h2 class="section-title" style="top:23px;left:10px">SIDE ORDERS</h2>
  <ul class="menu-list menu-list--two" style="top:63px">
    <li class="menu-item"><span>1. GYOZA 7PCS</span><span>4.45</span></li>
    <li class="menu-item"><span>2.EGG ROLL 3PCS</span><span>4.45</span></li>
    <li class="menu-item"><span>3. FRIED SHRIMP</span><span>4.45</span></li>
    <li class="menu-item"><span>4. CHICKEN TERIYAKI</span><span>5.95</span></li>
    <li class="menu-item"><span>5. BEEF TERIYAKI</span><span>5.95</span></li>
    <li class="menu-item"><span>6. PORK TERIYAKI</span><span>5.95</span></li>
    <li class="menu-item"><span>7. STEAM RICE</span><span>1.99</span></li>
    <li class="menu-item"><span>8. SALAD</span><span>3.50</span></li>
    <li class="menu-item"><span>9. MISO SOUP</span><span>1.99</span></li>
  </ul>

  <h2 class="section-title" style="top:227px">CHILDREN’S MEAL</h2>
  <ul class="menu-list menu-list--two" style="top:256px">
    <li class="menu-item"><span>CHICKEN OR BEEF W/RICE &amp; SALAD</span><span>6.25</span></li>
  </ul>

  <div class="photo-strip" style="top:294px">
    <div class="photo photo--chicken" role="img" aria-label="Photo of chicken teriyaki with mushrooms"></div>
    <div class="photo photo--curry" role="img" aria-label="Photo of rice with curry chicken"></div>
    <div class="photo photo--katsu" role="img" aria-label="Photo of chicken katsu with cabbage"></div>
    <div class="photo photo--gyoza" role="img" aria-label="Photo of gyoza dumplings on a plate"></div>
  </div>

  <div class="blossom" role="img" aria-label="Cherry blossom branch" style="left:-5px;top:400px;width:110px;height:90px"></div>

  <div class="brand" style="left:95px;top:425px;width:140px;height:36px">
    <span class="brand__name" style="font-size:18px">Kumo Garden</span>
  </div>

  <div class="map" role="img" aria-label="Street map showing the strip mall with lo-kart and the library next door"></div>

  <div class="location">
    <p><strong>OUR LOCATION</strong>2140 NE Alder St,<br>Fernwood, WA 98099<br>Phone: (425) 555-0142</p>
    <p><strong>OPEN</strong>Monday - Saturday<br>11AM - 8:30PM</p>
    <p><strong>Sunday closed</strong></p>
  </div>

  <div class="blossom" role="img" aria-label="Cherry blossom branch" style="left:240px;top:540px;width:110px;height:80px"></div>

  <svg class="cut-line" viewBox="0 0 329 10" aria-hidden="true">
    <line x1="0" y1="5" x2="329" y2="5" stroke="#ffffff" stroke-width="1" stroke-dasharray="6 4"/>
    <g transform="translate(62,0)" fill="none" stroke="#ffffff" stroke-width="1">
      <circle cx="3" cy="2.5" r="2"/><circle cx="3" cy="7.5" r="2"/>
      <line x1="4.5" y1="3.5" x2="16" y2="8"/><line x1="4.5" y1="6.5" x2="16" y2="2"/>
    </g>
  </svg>

  <div class="coupon__lead">TAKE ADDITIONAL</div>
  <div class="coupon__deal"><span class="pct">20%</span><span class="off">OFF</span></div>
  <p class="coupon__terms">
    By bring this brochure.<br>
    Not available with another<br>
    promotion or discount<br>
    <span class="coupon__valid">VALID UNTIL DECEMBER 2017</span>
    <span class="coupon__call">For Togo Order Call</span>
  </p>
  <div class="coupon__phone">(425) 555-0142</div>

  <div class="brand" style="left:232px;top:715px;width:70px;height:70px">
    <span class="brand__disc" style="width:70px;height:70px;left:0;top:0"></span>
    <span class="brand__name" style="font-size:14px">Kumo Garden</span>
  </div>
</section>

</body>
</html>
```